Our companies name is The Gilded Ladle and we specialize in craft cupcakes, what I mean by that is that we bake our cupcakes with craft beer and other alcoholic drinks. We are trying to focus on being elegant but at the same time unpretentious. Since we are incorporating beer in our cupcakes we want the business card to have our logo in the front and our information in the back.

Once we select the best design we will provide the contact information to be added. Thank you.

Industry/Entity Type

Business

Font styles to use
Decorative
Script

Requirements
Must have
• Round corners
Should not have
• Square corners

```html
<!DOCTYPE html>
<html lang="en">
<head>
<meta charset="utf-8">
<title>The Gilded Ladle – Business Card</title>
<link rel="stylesheet" href="https://fonts.googleapis.com/css2?family=Ubuntu:wght@400;500;700&display=swap">
<style>
  :root {
    --backdrop: #2a2a2c;
    --card-red: #e0282c;
    --card-black: #1b1b1c;
    --mint: #86d3b7;
    --mint-soft: #a9dfcb;
    --white: #f2f2f2;
    --card-radius: 20px;
  }
  * { box-sizing: border-box; margin: 0; padding: 0; }
  html, body {
    width: 1200px;
    height: 1000px;
    overflow: hidden;
    background: var(--backdrop);
    font-family: "Ubuntu", sans-serif;
  }
  .stage {
    position: relative;
    width: 1200px;
    height: 1000px;
  }
  .card {
    position: absolute;
    top: 340px;
    width: 540px;
    height: 320px;
    border-radius: var(--card-radius);
    overflow: hidden;
  }

  /* Back: contact details */
  .card-back {
    left: 40px;
    background: var(--card-black);
    color: var(--mint);
  }
  .accent-bar {
    position: absolute;
    left: 0;
    top: 52px;
    width: 12px;
    height: 124px;
    background: var(--card-red);
  }
  .holder {
    position: absolute;
    left: 52px;
    top: 44px;
  }
  .holder-name {
    font-size: 21px;
    font-weight: 700;
    letter-spacing: 0.2px;
  }
  .holder-role {
    margin-top: 4px;
    font-size: 14px;
    color: var(--mint-soft);
  }
  .divider {
    position: absolute;
    left: 240px;
    right: 0;
    top: 104px;
    height: 2px;
    background: var(--mint);
  }
  .contact-list {
    position: absolute;
    left: 52px;
    top: 126px;
    list-style: none;
    font-size: 16px;
    line-height: 27px;
    color: var(--mint-soft);
  }
  .brand {
    display: flex;
    align-items: center;
  }
  .brand-dot {
    border-radius: 50%;
    flex: none;
  }
  .brand-name {
    font-weight: 700;
    line-height: 1.05;
  }
  .back-brand {
    position: absolute;
    right: 28px;
    bottom: 28px;
    gap: 14px;
  }
  .back-brand .brand-dot {
    width: 64px;
    height: 64px;
    background: var(--card-red);
  }
  .back-brand .brand-name {
    font-size: 27px;
    color: var(--mint);
  }

  /* Front: brand */
  .card-front {
    left: 620px;
    background: var(--card-red);
    display: flex;
    align-items: center;
    justify-content: center;
  }
  .front-brand {
    gap: 24px;
  }
  .front-brand .brand-dot {
    width: 120px;
    height: 120px;
    background: var(--white);
  }
  .front-brand .brand-name {
    font-size: 54px;
    color: var(--card-black);
  }
</style>
</head>
<body>
  <main class="stage">
    <section class="card card-back" aria-label="Business card back">
      <div class="accent-bar"></div>
      <div class="holder">
        <p class="holder-name">Cardholder Name</p>
        <p class="holder-role">CEO &amp; Founder</p>
      </div>
      <div class="divider"></div>
      <ul class="contact-list">
        <li>add: your address goes here</li>
        <li>p : 000 0123 456</li>
        <li>e : emailid@gildedladle.com</li>
        <li>w : www.gildedladle.com</li>
      </ul>
      <div class="brand back-brand">
        <span class="brand-dot"></span>
        <span class="brand-name">The Gilded<br>Ladle</span>
      </div>
    </section>

    <section class="card card-front" aria-label="Business card front">
      <div class="brand front-brand">
        <span class="brand-dot"></span>
        <span class="brand-name">The Gilded<br>Ladle</span>
      </div>
    </section>
  </main>
</body>
</html>
```